private relaxation massage therapist business card

I want a card that does not give a physical address as I am able to massage at home as well as be mobile. I want on the back somewhere to put appointment details and also my bank acct details for payment being to acct 38 7402 0061948 00
I have a Certificate in Relaxation Massage from KPTA 2014
I would like to use blue colours and maybe have some fluffy clouds somewhere on the business card.

Industry/Entity Type

Massage

Contact Information for Business Card

Fiona Marsh
Relaxation Massage Therapist

telephone 0216 842 197 or 09 4718335
email fionamarsh72@quellbox.com

Requirements
Must have
• bold lettering, lots of white space, On the reverse of the card some lines in a box for me to write appointment times also on reverse my bank acct details for payment on line.

```html
<!DOCTYPE html>
<html lang="en">
<head>
<meta charset="utf-8">
<title>Fiona Marsh – Relaxation Massage Therapist</title>
<link rel="stylesheet" href="https://fonts.googleapis.com/css2?family=Fredoka:wght@600&family=Open+Sans:wght@400;600;700&display=swap">
<style>
  :root {
    --bg: #dcedfb;
    --card: #ffffff;
    --sky-deep: #5db8ee;
    --sky-mid: #9fd4f6;
    --sky-pale: #e6f4fd;
    --brand-blue: #1f8ad6;
    --brand-blue-dark: #1467b0;
    --navy: #16203a;
    --ink: #1b1b1b;
    --line: #8fa3b5;
    --frame: #5b8fd6;
  }
  * { box-sizing: border-box; margin: 0; padding: 0; }
  html, body { width: 1200px; height: 960px; overflow: hidden; }
  body {
    background: radial-gradient(ellipse at center, #f3f9ff 0%, var(--bg) 100%);
    font-family: "Open Sans", Arial, sans-serif;
    position: relative;
  }
  .card {
    position: absolute;
    left: 250px;
    width: 700px;
    height: 400px;
    background: var(--card);
    overflow: hidden;
    box-shadow: 0 8px 24px rgba(40, 90, 140, 0.18);
  }
  .card--front { top: 50px; }
  .card--back { top: 510px; }

  .sky {
    position: absolute;
    left: 0; top: 0; width: 100%;
    background: linear-gradient(180deg, var(--sky-deep) 0%, var(--sky-mid) 45%, var(--sky-pale) 80%, var(--card) 100%);
  }
  .card--front .sky { height: 200px; }
  .card--back .sky { height: 260px; }

  .portrait {
    position: absolute;
    border-radius: 40%;
    background: radial-gradient(ellipse at center, #e9c9b2 0%, #d8b49c 40%, rgba(220, 235, 248, 0) 75%);
  }
  .card--front .portrait { left: 260px; top: 20px; width: 210px; height: 160px; }
  .card--back .portrait { left: 30px; top: 60px; width: 180px; height: 130px; }

  .contact-tag {
    position: absolute;
    display: flex;
    align-items: center;
    gap: 10px;
    background: rgba(74, 166, 232, 0.85);
    border-radius: 6px;
    color: #fff;
    padding: 6px 12px;
  }
  .contact-tag--phone { left: 40px; top: 92px; }
  .contact-tag--email { right: 26px; top: 26px; padding: 6px 14px; }
  .contact-tag svg { flex: none; }
  .phone-lines { font-size: 16px; line-height: 19px; letter-spacing: 0.5px; }
  .email-text { font-size: 14px; }

  .brand {
    position: absolute;
    left: 0; top: 178px; width: 100%;
    text-align: center;
  }
  .brand__name {
    font-family: "Fredoka", "Open Sans", sans-serif;
    font-weight: 600;
    font-size: 58px;
    line-height: 1;
    color: var(--brand-blue);
  }
  .brand__role {
    display: inline-block;
    margin-top: 6px;
    background: var(--brand-blue);
    color: #fff;
    font-weight: 700;
    font-size: 21px;
    padding: 2px 18px;
    border-radius: 8px;
  }
  .brand__credential {
    margin-top: 8px;
    font-weight: 600;
    font-size: 20px;
    line-height: 25px;
    color: var(--brand-blue);
  }
  .brand__credential .body-name { color: var(--navy); }

  .appointment-box {
    position: absolute;
    left: 215px; top: 70px;
    width: 300px; height: 200px;
    border: 2px solid var(--frame);
    border-radius: 10px;
    background: rgba(255, 255, 255, 0.35);
    padding: 22px 14px;
    display: flex;
    flex-direction: column;
    justify-content: space-between;
  }
  .appointment-box .write-line {
    height: 0;
    border-top: 1px solid var(--line);
  }

  .payment {
    position: absolute;
    left: 0; top: 298px; width: 100%;
    text-align: center;
  }
  .payment__label { font-size: 24px; color: var(--ink); }
  .payment__account {
    display: inline-block;
    margin-top: 4px;
    background: linear-gradient(180deg, #6cc3f2, #3a9ee0);
    color: var(--navy);
    font-weight: 700;
    font-size: 20px;
    padding: 2px 14px;
    border-radius: 8px;
  }
</style>
</head>
<body>

<section class="card card--front">
  <div class="sky" role="img" aria-label="Blue sky with soft fluffy white clouds"></div>
  <div class="portrait" role="img" aria-label="Photo of a woman relaxing during a massage"></div>

  <div class="contact-tag contact-tag--phone">
    <svg width="26" height="26" viewBox="0 0 26 26" aria-hidden="true">
      <rect x="0" y="0" width="26" height="26" rx="4" fill="#fff"/>
      <path d="M8 6c-1 1-2 3 0 7s5 7 8 8c2 0.5 3-0.5 4-1.5l-3-3-2 1c-2-1-4-3-5-5l1-2-3-4z" fill="#1f8ad6"/>
    </svg>
    <div class="phone-lines">0216 842 197<br>09 4718335</div>
  </div>

  <div class="contact-tag contact-tag--email">
    <svg width="22" height="16" viewBox="0 0 22 16" aria-hidden="true">
      <rect x="1" y="1" width="20" height="14" rx="2" fill="#fff"/>
      <path d="M1 2l10 7 10-7" fill="none" stroke="#1f8ad6" stroke-width="1.6"/>
    </svg>
    <span class="email-text">fionamarsh72@quellbox.com</span>
  </div>

  <div class="brand">
    <div class="brand__name">Fiona Marsh</div>
    <div class="brand__role">Relaxation Massage Therapist</div>
    <div class="brand__credential">Certificate in Relaxation Massage<br>from <span class="body-name">KPTA</span> 2014</div>
  </div>
</section>

<section class="card card--back">
  <div class="sky" role="img" aria-label="Blue sky with soft fluffy white clouds"></div>
  <div class="portrait" role="img" aria-label="Photo of a woman relaxing during a massage"></div>

  <div class="appointment-box" aria-label="Appointment details">
    <div class="write-line"></div>
    <div class="write-line"></div>
    <div class="write-line"></div>
    <div class="write-line"></div>
    <div class="write-line"></div>
    <div class="write-line"></div>
  </div>

  <div class="payment">
    <div class="payment__label">My bank account for online payment</div>
    <div class="payment__account">acct 38 7402 0061948 00</div>
  </div>
</section>

</body>
</html>
```